Lantern Path Collective

Re-design our website www.lanternpathco.org
We are a non profit catering for adults, elderly, veterans and youth in impoverished neighborhoods to improve their digital access and help them improve their lives and better our community.

I need the text on home page to stay. Its the first message vsitors shd read when they arrive on our page.

Number of Pages Required

4 page

Font styles to use
Other font styles liked:
• color and font shd be like the image attched below.

```html
<!DOCTYPE html>
<html lang="en">
<head>
<meta charset="utf-8">
<title>Lantern Path Collective</title>
<link href="https://fonts.googleapis.com/css2?family=Nunito+Sans:wght@300;400;600;700&display=swap" rel="stylesheet">
<style>
:root{
  --ink:#3a3a3a;
  --ink-soft:#555;
  --white:#ffffff;
  --blue:#3a6aa8;
  --band:#6ea5c4;
  --peach:#f0c9a2;
  --peach-line:#f1c195;
  --green:#b9d07f;
  --green-line:#c5d69a;
  --green-btn:#8fb04e;
  --dark:#2a2a2a;
  --charcoal:#333333;
}
*{margin:0;padding:0;box-sizing:border-box}
html,body{width:1200px;height:3559px;overflow:hidden}
body{position:relative;background:var(--white);font-family:"Nunito Sans",Arial,sans-serif;color:var(--ink)}
.abs{position:absolute}

/* header */
.site-header{left:0;top:0;width:1200px;height:69px;background:var(--white)}
.brand-badge{left:184px;top:7px;width:158px;height:175px;border-radius:0 0 79px 79px;background:var(--white);z-index:5;display:flex;align-items:center;justify-content:center;text-align:center}
.brand-badge span{font-weight:700;font-size:17px;line-height:20px;color:var(--ink);width:120px}
.main-nav{right:200px;top:33px;display:flex;gap:26px;font-size:12px;color:var(--ink)}

/* hero */
.hero{left:0;top:69px;width:1200px;height:608px;background:linear-gradient(120deg,#2d2a28 0%,#5a4a42 35%,#8a8e94 60%,#c9c6bf 85%,#a9a39a 100%)}
.hero-panel{left:0;top:232px;width:541px;height:337px;background:rgba(20,16,14,.72)}
.hero-title{left:77px;top:304px;width:440px;font-weight:300;font-size:28.5px;line-height:34.5px;color:var(--white)}
.btn-learn{left:83px;top:460px;width:135px;height:33px;background:var(--blue);color:var(--white);font-size:12px;display:flex;align-items:center;justify-content:center}

/* intro */
.intro{left:269px;top:748px;width:662px;text-align:center;font-weight:600;font-size:14.2px;line-height:22.5px;color:#222}
.band{left:0;top:898px;width:1200px;height:154px;background:var(--band)}
.band p{position:absolute;left:345px;top:44px;width:540px;text-align:center;color:var(--white);font-weight:600;font-size:10.8px;line-height:20px}

/* story rows */
.story-img{background:linear-gradient(135deg,#d9d7d3,#9a8c80)}
.story-img.board{background:linear-gradient(135deg,#1f4a3c,#3f7a5e 50%,#b7a98a)}
.story-text{font-size:14.4px;line-height:21.3px;color:var(--ink)}

/* opportunities */
.peach-shape{left:0;top:1690px;width:1200px;height:910px}
.opp-title{left:254px;top:1972px;font-weight:600;font-size:27.5px;line-height:31.5px;color:var(--ink);letter-spacing:.3px}
.opp-text{left:254px;top:2128px;width:540px;font-size:13px;line-height:20px;color:var(--ink-soft)}
.donate-disc{left:701px;top:1702px;width:380px;height:380px;border-radius:50%;background:var(--white);border:3px solid var(--peach-line);overflow:hidden}
.disc-art{left:0;top:0;width:380px;height:235px;background:linear-gradient(180deg,#f2f5f1,#d2ddd4 60%,#b9c3c0)}
.disc-text{left:60px;top:246px;width:254px;text-align:center;font-weight:600;font-size:12.2px;line-height:15.4px;color:var(--ink)}
.btn-dark{left:142px;top:320px;width:97px;height:27px;background:var(--charcoal);color:var(--white);font-size:11px;display:flex;align-items:center;justify-content:center}
.card{width:200px;height:234px;background:var(--white)}
.card-img{left:0;top:0;width:200px;height:187px}
.card-icon{left:70px;top:157px;width:60px;height:60px;border-radius:50%;background:var(--white);display:flex;align-items:flex-start;justify-content:center;padding-top:12px}
.card-label{left:0;top:205px;width:200px;text-align:center;font-size:12px;color:#222}

/* donate section */
.donate-title{left:246px;top:2775px;font-weight:600;font-size:33px;line-height:41.5px;color:var(--ink)}
.donate-sub{left:250px;top:2918px;font-size:12.5px;line-height:18px;color:var(--ink-soft)}
.btn-green{left:249px;top:2966px;width:163px;height:31px;background:var(--green);color:#2d3a18;font-size:11.5px;display:flex;align-items:center;justify-content:center}
.truck-art{left:596px;top:2752px;width:580px;height:410px;border-radius:8px;background:linear-gradient(160deg,#4d5f34,#6e7d4e 45%,#c9c3b6 70%,#7f9a68)}

/* footer */
.site-footer{left:0;top:3227px;width:1200px;height:332px;background:linear-gradient(180deg,#2b2b2b 0%,#2f2e2c 45%,#4a4640 100%)}
.footer-badge{left:66px;top:3187px;width:152px;height:152px;border-radius:50%;background:#0f0f0f;display:flex;align-items:center;justify-content:center;text-align:center}
.footer-badge span{color:var(--white);font-weight:700;font-size:15px;line-height:18px;width:110px}
.f-col h4{font-size:10.5px;font-weight:700;letter-spacing:.6px;color:var(--white);margin-bottom:11px}
.f-col li{list-style:none;font-size:10.8px;color:#d4d4d4;line-height:21.3px}
.btn-foot{left:733px;top:3400px;width:96px;height:28px;background:var(--green-btn);color:var(--white);font-size:11px;display:flex;align-items:center;justify-content:center}
.legal{left:250px;top:3474px;font-size:9.8px;line-height:21px;color:var(--white)}
.social{left:735px;top:3488px;display:flex;gap:6px}
.social span{width:22px;height:22px;border-radius:50%;background:var(--white)}
</style>
</head>
<body>

<header class="abs site-header">
  <nav class="abs main-nav">
    <span>Home</span><span>Get Connected</span><span>e-Waste Services</span><span>Our Impact</span><span>About</span><span>Contact</span><span>Donate</span>
  </nav>
</header>
<div class="abs brand-badge"><span>Lantern Path Collective</span></div>

<section class="abs hero" role="img" aria-label="Photo of a child working on a laptop at a desk"></section>
<div class="abs hero-panel"></div>
<h1 class="abs hero-title">Creating a Social Impact with e-Waste by transforming Unwanted Technology into Opportunities for People In-Need.</h1>
<div class="abs btn-learn">Learn more</div>

<p class="abs intro">Lantern Path Collective is a nonprofit and social enterprise that creates equitable access to opportunity by providing devices, internet access, digital skills training, and tech support for low-income families, the homeless, and Veterans in our communities while at the same time, empowering businesses and organizations to do good by diverting technology from landfills to protect our planet.</p>

<section class="abs band"><p>Being digitally literate is no longer a luxury, it is a must-have skill for everyone to manage information, communicate, manage money, and access support plus other government services. It has become an essential tool for modern-day citizenship and participation; no one can afford to be left behind.</p></section>

<div class="abs story-img" style="left:180px;top:1117px;width:367px;height:274px" role="img" aria-label="Photo of two children smiling at a computer"></div>
<p class="abs story-text" style="left:586px;top:1132px;width:360px">Unfortunately, nearly 100 million Americans lack access to a personal computer, internet connection, or both. This lack of access to digital technology creates a significant gap between the opportunities unconnected people can access and the ones digitally native households can. This gap in opportunities is known as the digital divide, and it’s our mission by joining hands with many other organizations that are tirelessly trying to shrink it because we believe that equitable access to information and technology empowers people to achieve their fullest potential.</p>

<div class="abs story-img board" style="left:180px;top:1439px;width:367px;height:236px" role="img" aria-label="Photo of discarded circuit boards and a processor chip"></div>
<p class="abs story-text" style="left:593px;top:1454px;width:368px">At the same time Electronic waste, or e-waste, refers to electronic products and components that are unwanted, unusable, or nearing the end of their useful life. While e-waste only makes up 2% of the mass in landfills, it accounts for 70% of of toxic waste. Unfortunately, recycling is no longer a sufficient method for disposing of waste sustainably; given the scale of the climate crisis, reuse is now a prerequisite for protecting our planet.</p>

<svg class="abs peach-shape" viewBox="0 0 1200 910" width="1200" height="910" aria-hidden="true">
  <path d="M0 160 C 300 130, 620 120, 900 175 C 1020 200, 1110 230, 1200 262 L1200 910 L0 910 Z" fill="#f0c9a2"/>
</svg>

<div class="abs donate-disc">
  <div class="abs disc-art" role="img" aria-label="Illustration of discarded appliances and electronics before a city skyline"></div>
  <p class="abs disc-text">Donate your e-waste and help us empower people with the digital tools, resources, and support they need to unlock their full potential.</p>
  <div class="abs btn-dark">Donate now</div>
</div>

<h2 class="abs opp-title">Explore Opportunities<br>Online with Low-Cost<br>Technology, Internet, Training<br>&amp; Support</h2>
<p class="abs opp-text">In order to comprehensively shrink the digital divide, we offer you access to low-cost computers, low-cost internet, free digital literacy training and tech support. Click the boxes below to explore how we can help you and members of your community unlock their full potential through digital technology.</p>

<div class="abs card" style="left:160px;top:2292px">
  <div class="abs card-img" style="background:linear-gradient(135deg,#c9c4bc,#7d7870)" role="img" aria-label="Photo of a young man using a laptop"></div>
  <div class="abs card-icon"><svg width="30" height="22" viewBox="0 0 30 22" fill="none" stroke="#555" stroke-width="1.3"><rect x="6" y="2" width="18" height="13"/><path d="M2 19h26"/><path d="M11 11l8-6"/></svg></div>
  <div class="abs card-label">Affordable Technology</div>
</div>
<div class="abs card" style="left:387px;top:2292px">
  <div class="abs card-img" style="background:linear-gradient(135deg,#d8d6d2,#6e6560)" role="img" aria-label="Photo of hands typing on a laptop"></div>
  <div class="abs card-icon"><svg width="30" height="22" viewBox="0 0 30 22" fill="none" stroke="#555" stroke-width="1.3"><path d="M3 8a17 17 0 0 1 24 0"/><path d="M7 12a11 11 0 0 1 16 0"/><path d="M11 16a5 5 0 0 1 8 0"/><circle cx="15" cy="19" r="1" fill="#555"/></svg></div>
  <div class="abs card-label">Internet Access</div>
</div>
<div class="abs card" style="left:612px;top:2292px">
  <div class="abs card-img" style="background:linear-gradient(135deg,#e2d3bf,#6f86a6)" role="img" aria-label="Photo of a young woman helping an older woman at a computer"></div>
  <div class="abs card-icon"><svg width="30" height="26" viewBox="0 0 30 26" fill="none" stroke="#555" stroke-width="1.3"><path d="M15 5a6 6 0 0 0-3.5 10.9V19h7v-3.1A6 6 0 0 0 15 5z"/><path d="M12 22h6"/><path d="M15 1v2M5 9H3M27 9h-2M7 3l1.5 1.5M23 3l-1.5 1.5"/></svg></div>
  <div class="abs card-label">Digital Literacy Training</div>
</div>
<div class="abs card" style="left:841px;top:2292px">
  <div class="abs card-img" style="background:linear-gradient(135deg,#cfd6d8,#6f7d85)" role="img" aria-label="Photo of support agents wearing headsets"></div>
  <div class="abs card-icon"><svg width="30" height="28" viewBox="0 0 30 28" fill="none" stroke="#555" stroke-width="1.3"><rect x="5" y="1" width="13" height="9"/><rect x="12" y="5" width="13" height="9"/><circle cx="9" cy="18" r="2.5"/><circle cx="21" cy="18" r="2.5"/><path d="M4 26a5 5 0 0 1 10 0M16 26a5 5 0 0 1 10 0"/></svg></div>
  <div class="abs card-label">Tech Support</div>
</div>

<svg class="abs" style="left:270px;top:2680px" width="380" height="380" viewBox="0 0 380 380" aria-hidden="true">
  <circle cx="190" cy="186" r="180" fill="none" stroke="#c5d69a" stroke-width="2"/>
</svg>
<svg class="abs" style="left:815px;top:2960px" width="330" height="230" viewBox="0 0 330 230" aria-hidden="true">
  <path d="M10 10 A 160 160 0 0 0 320 70" fill="none" stroke="#f1c195" stroke-width="2"/>
</svg>

<div class="abs truck-art" role="img" aria-label="Illustration of two people loading donated electronics into a recycling van beside a pile of circuit boards"></div>

<h2 class="abs donate-title">Donate Your<br>Unwanted Technology.<br>Change People’s Lives.</h2>
<p class="abs donate-sub">Donate Your Technology to Make an Impact on<br>Your Community</p>
<div class="abs btn-green">I’m ready to donate</div>

<footer class="abs site-footer" role="img" aria-label="Faint background photo of piled electronic waste"></footer>
<div class="abs footer-badge"><span>Lantern Path Collective</span></div>

<div class="abs f-col" style="left:244px;top:3300px"><h4>GET CONNECTED</h4><ul><li>Get Technology</li><li>Low-Cost Internet</li><li>Digital Training</li><li>Tech Support</li><li>For Organizations</li></ul></div>
<div class="abs f-col" style="left:427px;top:3300px"><h4>REPURPOSE YOUR TECH</h4><ul><li>E-Waste Services</li><li>Data Destruction</li><li>Technology Drives</li></ul></div>
<div class="abs f-col" style="left:609px;top:3300px"><h4>ABOUT</h4><ul><li>About</li><li>Our Impact</li></ul></div>
<div class="abs f-col" style="left:733px;top:3300px"><h4>CONTACT</h4><ul><li>(555) 014-2270</li><li>hello@lanternpathco.org</li><li>418 Harbor Row, Fairview, CA 90000</li></ul></div>
<div class="abs btn-foot">Donate</div>

<p class="abs legal">Privacy &amp; Security Policy<br>© 2023 by Lantern Path Collective. All rights reserved.</p>
<div class="abs social" aria-label="Social links"><span></span><span></span><span></span><span></span></div>

</body>
</html>
```